Swimming Pool Supply Company Business Cards

We need business cards designed for company. These need to be easy to edit so that we can fill in names, titles, and contact info for each person who works here.

Dalton R. Whitfield
Manager of Legal & Finance
K.L. Brisbane, Incorporated

4837 Grenway Avenue
Marlow Heights, PA 19243

E. dalton@klbrisbane-example.com
M. (215) 555-0173
O. (215) 555-0148

Contact Information for Business Card

Looking to upgrade current business cards with graphic that can be edited. Looking for fresh ideas for an age old industry.

Font styles to use
Serif
Sans Serif

Colors

Designer to choose colors to be used in the design.

Requirements
Must have
• Professional, fresh, unique but professional

```html
<!DOCTYPE html>
<html lang="en">
<head>
<meta charset="utf-8">
<title>K.L. Brisbane Business Card</title>
<link rel="stylesheet" href="https://fonts.googleapis.com/css2?family=Cabin:wght@400;600;700&display=swap">
<style>
  :root {
    --brand-blue: #0043f7;
    --paper: #ffffff;
    --ink: #111111;
  }
  * { margin: 0; padding: 0; box-sizing: border-box; }
  html, body { width: 1200px; height: 1200px; overflow: hidden; background: var(--paper); }
  body { position: relative; font-family: "Cabin", "Segoe UI", sans-serif; color: var(--brand-blue); }

  .card { position: absolute; left: 74px; width: 870px; height: 511px; }
  .card-front { top: 67px; border: 1.5px solid var(--ink); background: var(--paper); }
  .card-back { top: 622px; border: 1.5px solid var(--ink); background: var(--brand-blue); }

  .front-frame {
    position: absolute; left: 12px; top: 11px; width: 846px; height: 488px;
    border: 6px solid var(--brand-blue);
  }
  .back-frame { position: absolute; left: 0; top: 0; }

  .wordmark { position: absolute; }
  .wordmark text { font-family: "Cabin", sans-serif; font-weight: 700; }
  .front-wordmark { left: 56px; top: 60px; }
  .back-wordmark { left: 110px; top: 165px; }

  .company-name {
    position: absolute; left: 68px; top: 150px;
    font-size: 26px; font-weight: 700; white-space: nowrap;
  }

  .person { position: absolute; right: 64px; top: 196px; text-align: right; }
  .person-name { font-size: 30px; font-weight: 700; line-height: 36px; }
  .person-title { font-size: 21px; line-height: 28px; margin-right: 0; }

  .icon-box {
    position: absolute; width: 28px; height: 28px; background: var(--brand-blue);
    display: flex; align-items: center; justify-content: center;
  }
  .icon-box svg { width: 22px; height: 22px; }

  .contact-line {
    position: absolute; right: 84px; font-size: 23px; white-space: nowrap; line-height: 28px;
  }

  .tagline {
    position: absolute; left: 0; width: 870px; top: 305px; text-align: center;
    font-size: 30px; color: var(--paper); white-space: nowrap;
  }

  .side-label {
    position: absolute; font-size: 56px; color: var(--ink); font-weight: 400;
  }
</style>
</head>
<body>

  <section class="card card-front">
    <div class="front-frame"></div>

    <svg class="wordmark front-wordmark" width="340" height="72" viewBox="0 0 340 72">
      <text x="0" y="66" font-size="74" fill="var(--brand-blue)" textLength="338" lengthAdjust="spacingAndGlyphs">BRISBANE</text>
    </svg>
    <div class="company-name">K.L. Brisbane, Incorporated</div>

    <div class="person">
      <div class="person-name" style="margin-right:42px">Dalton R. Whitfield</div>
      <div class="person-title" style="margin-right:42px">Manager of Legal &amp; Finance</div>
    </div>
    <div class="icon-box" style="left:803px; top:202px;">
      <svg viewBox="0 0 22 22"><circle cx="11" cy="8" r="4.5" fill="#fff"/><path d="M3 21c0-5 3.5-7.5 8-7.5s8 2.5 8 7.5z" fill="#fff"/></svg>
    </div>

    <div class="contact-line" style="top:315px;">(215) 555-0173</div>
    <div class="icon-box" style="left:803px; top:315px;">
      <svg viewBox="0 0 22 22"><path d="M7 3c-2 1-3 3-2 6 1 4 4 8 8 10 2 1 4 0 5-1l-3-3-2 1c-2-1-4-4-5-6l1-2z" fill="none" stroke="#fff" stroke-width="1.6"/></svg>
    </div>

    <div class="contact-line" style="top:359px;">(215) 555-0148</div>
    <div class="icon-box" style="left:803px; top:359px;">
      <svg viewBox="0 0 22 22"><path d="M2 9c0-3 4-4 9-4s9 1 9 4l-4 1-1-2H7L6 10z" fill="#fff"/><path d="M6 11h10l2 6H4z" fill="#fff"/><circle cx="11" cy="14" r="1.8" fill="var(--brand-blue)"/></svg>
    </div>

    <div class="contact-line" style="top:403px;">dalton@klbrisbane-example.com</div>
    <div class="icon-box" style="left:803px; top:403px;">
      <svg viewBox="0 0 22 22"><rect x="3" y="6" width="16" height="11" fill="none" stroke="#fff" stroke-width="1.6"/><path d="M3 6l8 6 8-6" fill="none" stroke="#fff" stroke-width="1.6"/></svg>
    </div>

    <div class="contact-line" style="top:447px;">4837 Grenway Avenue Marlow Heights, PA 19243</div>
    <div class="icon-box" style="left:803px; top:447px;">
      <svg viewBox="0 0 22 22"><path d="M11 17s-5-5-5-9a5 5 0 0 1 10 0c0 4-5 9-5 9z" fill="none" stroke="#fff" stroke-width="1.6"/><circle cx="11" cy="8" r="1.8" fill="#fff"/><path d="M6 19h10" stroke="#fff" stroke-width="1.6"/></svg>
    </div>
  </section>

  <section class="card card-back">
    <svg class="back-frame" width="870" height="511" viewBox="0 0 870 511">
      <path d="M14 15H855V496H14" fill="none" stroke="var(--paper)" stroke-width="6"/>
    </svg>
    <svg class="wordmark back-wordmark" width="650" height="130" viewBox="0 0 650 130">
      <text x="0" y="124" font-size="150" fill="var(--paper)" textLength="650" lengthAdjust="spacingAndGlyphs">BRISBANE</text>
    </svg>
    <div class="tagline">Big Enough to Serve You, Small Enough to Care</div>
  </section>

  <div class="side-label" style="left:994px; top:305px;">Front</div>
  <div class="side-label" style="left:976px; top:795px;">Back</div>

</body>
</html>
```